Business Card Design Project

restaurant management company needs business card design.

Industry/Entity Type

Restaurant

Requirements
Must have
• our logo
Quillfern logo
RWJ logo
Marrow Bay Logo
Nice to have
• Corwin Tally
(position)

283 Maplerow Street
Ellisford EM,
Canada
K2R 8J4

Tel 555-xxx-xxxx Ext 201
Fax 555-xxx-xxxx
Mobile 555-xxx-xxxx

corwintally@brelvanco.ca
Should not have
• Corwin Tally
(position)

283 Maplerow Street
Ellisford EM,
Canada
K2R 8J4

Tel 555-xxx-xxxx Ext 201
Fax 555-xxx-xxxx
Mobile 555-xxx-xxxx

corwintally@brelvanco.ca

```html
<!DOCTYPE html>
<html lang="en">
<head>
<meta charset="utf-8">
<title>Brelvanco Business Card</title>
<link rel="stylesheet" href="https://fonts.googleapis.com/css2?family=Arimo:wght@400;700&display=swap">
<style>
  :root {
    --red: #e41f26;
    --red-deep: #7a0d10;
    --red-faint: #f26a6f;
    --black: #000000;
    --ink: #231f20;
    --white: #ffffff;
    --stage: #e6e6e6;
    --font: "Arimo", Arial, sans-serif;
  }
  * { box-sizing: border-box; margin: 0; padding: 0; }
  html, body { width: 1200px; height: 900px; overflow: hidden; }
  body {
    background: var(--stage);
    font-family: var(--font);
    position: relative;
  }
  .card {
    position: absolute;
    left: 250px;
    width: 700px;
    height: 400px;
    overflow: hidden;
  }
  .card-front { top: 35px; background: var(--black); }
  .card-back { top: 465px; background: var(--white); }
  .card-art { position: absolute; inset: 0; width: 100%; height: 100%; }

  .brand-mark {
    position: absolute;
    display: flex;
    align-items: center;
    gap: 10px;
    font-weight: 700;
    letter-spacing: -0.5px;
    white-space: nowrap;
  }
  .brand-dot { width: 16px; height: 16px; border-radius: 50%; background: var(--red); flex: none; }
  .card-front .brand-mark {
    left: 0; right: 0; top: 172px;
    justify-content: center;
    color: var(--white);
    font-size: 50px;
  }
  .card-back .brand-mark {
    left: 62px; top: 96px;
    color: var(--ink);
    font-size: 30px;
    gap: 8px;
  }
  .card-back .brand-mark .brand-dot {
    width: 12px; height: 12px;
    background: var(--white);
    border: 2px solid var(--ink);
  }

  .brand-ghost {
    position: absolute;
    left: 70px; top: 300px;
    font-size: 32px;
    font-weight: 700;
    letter-spacing: -0.5px;
    color: var(--red-faint);
    white-space: nowrap;
  }

  .holder {
    position: absolute;
    left: 424px; top: 40px;
    color: var(--ink);
  }
  .holder-name { font-size: 24px; font-weight: 700; color: var(--white); white-space: nowrap; }
  .holder-role { font-size: 15px; font-weight: 700; margin-left: 120px; margin-top: 2px; }
  .holder-address {
    font-size: 11px; font-weight: 700; line-height: 1.3;
    margin-left: 120px; margin-top: 8px; font-style: normal;
  }

  .contact {
    position: absolute;
    left: 247px; top: 196px;
    font-size: 14px; font-weight: 700;
    line-height: 1.3;
  }
  .contact-row { display: flex; }
  .contact-label { width: 64px; color: var(--red); }
  .contact-value { color: var(--ink); }
  .contact-email { color: var(--red); }

  .partners {
    position: absolute;
    right: 22px; bottom: 26px;
    display: flex; gap: 22px;
    font-size: 13px; font-weight: 700;
    color: var(--red);
  }
</style>
</head>
<body>

  <section class="card card-front" aria-label="Card front">
    <svg class="card-art" viewBox="0 0 700 400" aria-hidden="true">
      <defs>
        <linearGradient id="band-fade" x1="0" y1="0" x2="0" y2="1">
          <stop offset="0" stop-color="#e41f26"/>
          <stop offset="1" stop-color="#7a0d10"/>
        </linearGradient>
      </defs>
      <rect x="236" y="0" width="244" height="120" fill="#e41f26"/>
      <rect x="236" y="250" width="244" height="150" fill="url(#band-fade)"/>
    </svg>
    <div class="brand-mark"><span class="brand-dot"></span>Brelvanco</div>
  </section>

  <section class="card card-back" aria-label="Card back">
    <svg class="card-art" viewBox="0 0 700 400" aria-hidden="true">
      <rect x="57" y="0" width="183" height="400" fill="#e41f26"/>
      <polygon points="240,0 700,0 700,165 430,178 395,20 240,24" fill="#e41f26"/>
      <path d="M240 300 C 420 290, 560 282, 700 272" stroke="#e41f26" stroke-width="2" fill="none"/>
    </svg>
    <div class="brand-mark"><span class="brand-dot"></span>Brelvanco</div>
    <div class="brand-ghost">Brelvanco</div>

    <div class="holder">
      <p class="holder-name">Corwin Tally</p>
      <p class="holder-role">Position</p>
      <address class="holder-address">
        283 Maplerow Street<br>
        Ellisford EM,<br>
        Canada<br>
        K2R 8J4
      </address>
    </div>

    <div class="contact">
      <p class="contact-row"><span class="contact-label">Tel</span><span class="contact-value">555-xxx-xxxx Ext 201</span></p>
      <p class="contact-row"><span class="contact-label">Fax</span><span class="contact-value">555-xxx-xxxx</span></p>
      <p class="contact-row"><span class="contact-label">Mobile</span><span class="contact-value">555-xxx-xxxx</span></p>
      <p class="contact-email">corwintally@brelvanco.ca</p>
    </div>

    <div class="partners">
      <span>RWJ</span>
      <span>Marrow Bay</span>
      <span>Quillfern</span>
    </div>
  </section>

</body>
</html>
```